Electrical panel service sticker w Bucket truck & Logo

We have a rather plain sticker we put on lighting panels to remind customers who to call for service. We want to redesign them with brushed aluminum background. We want a remake of the sticker with the outline of a bucket truck. You'll need to find or draw the outling of a bucket truck maybe with the boom up slightly as we will get these stickers die cut.

We want LOGO with Ph.# and Email.
Electrical * Lighting * Sign Service

Target Market(s)

Commercial property managers

Industry/Entity Type

Property Management

Requirements
Must have
• Bucket Truck Outline

```html
<!DOCTYPE html>
<html lang="en">
<head>
<meta charset="utf-8">
<title>Beacon Lightworks Panel Service Sticker</title>
<link rel="stylesheet" href="https://fonts.googleapis.com/css2?family=Roboto:wght@500;700;900&display=swap">
<style>
  :root {
    --brand-red: #f2051d;
    --ink: #333333;
    --band-text: #ffffff;
    --steel-dark: #a7a7a9;
    --steel-mid: #c3c3c5;
    --steel-light: #eeeeef;
    --truck-tone: #b9b9bb;
  }
  * { margin: 0; padding: 0; box-sizing: border-box; }
  html, body { width: 1200px; height: 1200px; overflow: hidden; }
  body { font-family: "Roboto", Arial, sans-serif; }

  .sticker {
    position: relative;
    width: 1200px;
    height: 1200px;
    background:
      repeating-linear-gradient(0deg, rgba(255,255,255,0.06) 0 1px, rgba(0,0,0,0.04) 1px 3px),
      linear-gradient(180deg, var(--steel-dark) 0%, var(--steel-mid) 30%, var(--steel-light) 48%, var(--steel-mid) 66%, var(--steel-dark) 100%);
  }

  .brand-name {
    position: absolute;
    top: 40px;
    left: 0;
    width: 100%;
    text-align: center;
    color: var(--brand-red);
    font-weight: 900;
    text-transform: uppercase;
    line-height: 1;
  }
  .brand-name .line-one { display: block; font-size: 128px; letter-spacing: 2px; }
  .brand-name .line-two { display: block; font-size: 128px; margin-top: 22px; letter-spacing: 1px; }

  .truck-art {
    position: absolute;
    left: 276px;
    top: 358px;
    width: 650px;
    height: 422px;
    border-radius: 10px;
    background: linear-gradient(180deg, rgba(185,185,187,0.55), rgba(160,160,162,0.55));
  }

  .contact-email {
    position: absolute;
    top: 808px;
    left: 0;
    width: 100%;
    text-align: center;
    font-weight: 500;
    font-size: 57px;
    color: var(--ink);
  }
  .contact-phone {
    position: absolute;
    top: 880px;
    left: 0;
    width: 100%;
    text-align: center;
    font-weight: 900;
    font-size: 136px;
    letter-spacing: 2px;
    color: var(--ink);
    line-height: 1.2;
  }

  .service-band {
    position: absolute;
    left: 0;
    bottom: 0;
    width: 100%;
    height: 166px;
    background: var(--brand-red);
    color: var(--band-text);
    font-weight: 700;
    font-size: 51px;
    text-align: center;
    display: flex;
    flex-direction: column;
    justify-content: center;
    gap: 8px;
    line-height: 1.1;
  }
</style>
</head>
<body>
  <main class="sticker">
    <h1 class="brand-name">
      <span class="line-one">Beacon</span>
      <span class="line-two">Lightworks</span>
    </h1>

    <div class="truck-art" role="img" aria-label="Line-drawn outline of a utility bucket truck with its boom raised"></div>

    <p class="contact-email">Service@BeaconLightworks.com</p>
    <p class="contact-phone">877-555-0148</p>

    <div class="service-band">
      <p>• Roadways • Commercial</p>
      <p>• Sportslighting • Electrical &nbsp;• Signs</p>
    </div>
  </main>
</body>
</html>
```